Brochure & Flyer Design

Tidewell Harlow - Fish & Chips is a popular fish and chip store located on Sydney’s beautiful northern beaches. It sits just across from the sandy shores of Newport Beach.
Please see attached:
1. Details on the brochure I would like designed for Tidewell Harlow
2. Current menu that is in store that will need to be included
3. Logo
I would like a modern, fresh design to complement the logo focusing on the food.
Here is the link to download the images that should be included in the brochure https://www.sendvaulty.net/download/Xk7pQm2LrT9wVbN4ZsYhJe
To complement the brochure I would like an A1 flyer template that can be used to promote specials at the store.

```html
<!DOCTYPE html>
<html lang="en">
<head>
<meta charset="utf-8">
<title>Tidewell Harlow - Fish &amp; Chips Menu</title>
<link rel="stylesheet" href="https://fonts.googleapis.com/css2?family=Anton&family=Comfortaa:wght@400;700&family=Lobster&family=Oswald:wght@700&display=swap">
<style>
:root{
  --orange:#f15a24;
  --orange-panel:#e04c1f;
  --navy:#283a7a;
  --navy-text:#1f2d6b;
  --white:#ffffff;
  --yellow-1:#ffd84a;
  --yellow-2:#f9a51a;
  --ink:#1a1a1a;
}
*{margin:0;padding:0;box-sizing:border-box}
html,body{width:1200px;height:927px;overflow:hidden}
body{position:relative;background:var(--white);font-family:"Comfortaa",sans-serif;color:var(--white)}
.menu-top{position:absolute;left:0;top:0;width:1200px;height:422px;background:var(--orange)}
.menu-bottom{position:absolute;left:0;top:422px;width:1200px;height:433px;background:var(--navy)}
.footer{position:absolute;left:0;top:855px;width:1200px;height:72px;background:var(--white);color:var(--ink);font-family:"Comfortaa",sans-serif;font-size:15px;white-space:nowrap;display:flex;align-items:center;justify-content:center;gap:8px}
.footer .social-name{font-size:15px;color:var(--ink)}
.panel{position:absolute;top:40px;height:382px;background:var(--orange-panel);border-radius:20px 20px 0 0}
.panel-family{left:28px;width:270px}
.panel-fish{left:316px;width:282px}
.panel-burgers{left:616px;width:270px}
.panel-pack{left:906px;width:270px}
.heading{position:absolute;font-family:"Anton",sans-serif;font-size:31px;line-height:1;letter-spacing:.3px;font-weight:400}
.item{position:absolute;font-weight:700;font-size:22px;line-height:1}
.desc{position:absolute;font-size:14.5px;line-height:19.5px}
.badge{position:absolute;width:74px;height:74px;border-radius:50%;background:radial-gradient(circle at 40% 35%,var(--yellow-1),var(--yellow-2));border:4px solid var(--white);box-shadow:0 2px 4px rgba(0,0,0,.3);display:flex;align-items:center;justify-content:center;font-family:"Oswald",sans-serif;font-weight:700;font-size:18px;color:var(--navy-text);transform:translate(-50%,-50%)}
.pack-list{position:absolute;left:937px;top:115px;font-size:14px;line-height:19.8px}
.pack-prices{position:absolute;left:1088px;top:106px;width:62px;height:294px;background:var(--white);border-radius:4px;color:var(--navy-text);font-size:14.5px;line-height:19.8px;padding:9px 0 0 12px}
.card{position:absolute;top:463px;width:178px;height:120px;background:var(--orange);border-radius:16px 16px 0 0;text-align:center;padding:12px 4px 0}
.card h3{font-family:"Lobster",sans-serif;font-weight:400;font-size:19px;line-height:22px}
.card p{font-size:11.5px;line-height:16px;margin-top:2px}
.photo{position:absolute;top:560px;width:157px;height:238px;border:4px solid var(--white);background:linear-gradient(160deg,#cfe0ee 0%,#e7a34b 45%,#d9822b 100%)}
.card-badge{top:628px}
</style>
</head>
<body>
<section class="menu-top">
  <div class="panel panel-family"></div>
  <div class="panel panel-fish"></div>
  <div class="panel panel-burgers"></div>
  <div class="panel panel-pack"></div>

  <h2 class="heading" style="left:46px;top:80px">Family Meals</h2>
  <div class="item" style="left:46px;top:124px">Fishermans Basket</div>
  <p class="desc" style="left:46px;top:156px">2 Fillets of Fish, 6 Calamari<br>Rings, 4 Prawns, 4 Sea<br>Scallops, Large Chips,<br>Lemon &amp; Sauce</p>
  <div class="badge" style="left:258px;top:208px">$39.90</div>
  <div class="item" style="left:46px;top:245px">Dinner Pack</div>
  <p class="desc" style="left:46px;top:270px">4 Fillets of Fish, 12<br>Calamari<br>Rings, Large Chips,<br>Lemon &amp; Sauce</p>
  <div class="badge" style="left:248px;top:312px">$39.90</div>

  <h2 class="heading" style="left:333px;top:80px">Daily Market Fish</h2>
  <div class="item" style="left:335px;top:125px">Grilled or Fried</div>
  <p class="desc" style="left:335px;top:150px">Salmon<br>Barramundi<br>Snapper</p>
  <div class="badge" style="left:547px;top:164px">$16.90</div>
  <div class="item" style="left:335px;top:241px">With Chips</div>
  <div class="badge" style="left:547px;top:263px">$19.90</div>
  <div class="item" style="left:335px;top:306px">Salads</div>
  <p class="desc" style="left:335px;top:330px">Coleslaw Salad<br>Garden Salad</p>
  <div class="badge" style="left:545px;top:345px">$6.90</div>

  <h2 class="heading" style="left:638px;top:64px">Burgers</h2>
  <div class="item" style="left:643px;top:106px">Outrigger Burger</div>
  <p class="desc" style="left:643px;top:132px">4 Calamari Rings, Garden<br>Lettuce &amp; Tartare Sauce</p>
  <div class="item" style="left:643px;top:181px">Odessey Burger</div>
  <p class="desc" style="left:643px;top:206px;font-size:13.5px">Fish Fillet, Coleslaw Salad<br>&amp; Seafood Sauce</p>
  <div class="badge" style="left:869px;top:215px">$7.90</div>
  <div class="item" style="left:643px;top:253px">Olympiad Burger</div>
  <p class="desc" style="left:643px;top:278px;font-size:14px">Fish Fillet, Fresh Tomato, Garden<br>Lettuce &amp; Tartare Sauce<br>Grilled + $2</p>
  <div class="item" style="left:643px;top:343px">Burger Combo</div>
  <p class="desc" style="left:643px;top:368px">Choose Any burger with<br>chips and 600ml water</p>
  <div class="badge" style="left:877px;top:361px">$12.90</div>

  <h2 class="heading" style="left:935px;top:64px">Create a Pack</h2>
  <p class="pack-list">Fillet of Fish<br>Fish Cokctail<br>calamari Ring<br>Prawn Cutlet<br>Sea Sxallop<br>Ocean Mussel<br>seafood Stick<br>Small Chips<br>Large Chips<br>Potato Scallop<br>Bananaa Fritter<br>Pineapple Fritter<br>Vegie Spring Roll<br>Extra Sauce</p>
  <p class="pack-prices">$8.90<br>$2.40<br>$1.00<br>$2.40<br>$2.40<br>$1.00<br>$1.80<br>$4.50<br>$7.00<br>$1.00<br>$3.00<br>$3.00<br>$2.50<br>50C</p>
</section>

<section class="menu-bottom"></section>

<div class="card" style="left:24px"><h3>Fish Cocktail<br>Pack</h3><p>6 Fish Cocktails and Chips</p></div>
<div class="photo" role="img" aria-label="Photo of calamari rings and chips with tartare sauce" style="left:35px"></div>
<div class="badge card-badge" style="left:193px">$13.90</div>

<div class="card" style="left:217px"><h3>Junior Pack</h3><p>2 Fish Cocktails, 2 Calamari Rings, 1 Seafood Stick and CHipsa</p></div>
<div class="photo" role="img" aria-label="Photo of calamari rings and chips with tartare sauce" style="left:228px"></div>
<div class="badge card-badge" style="left:386px">$9.90</div>

<div class="card" style="left:410px"><h3>Calamari Pack</h3><p>8 Calamari Rings and Chips</p></div>
<div class="photo" role="img" aria-label="Photo of calamari rings and chips with tartare sauce" style="left:421px"></div>
<div class="badge card-badge" style="left:579px">$11.90</div>

<div class="card" style="left:603px"><h3>Fish &amp; Chips</h3><p>1 Fillet of Fish and CHips Grilled + $2</p></div>
<div class="photo" role="img" aria-label="Photo of calamari rings and chips with tartare sauce" style="left:614px"></div>
<div class="badge card-badge" style="left:772px">$11.90</div>

<div class="card" style="left:796px"><h3 style="margin-top:10px">Prawn Pack</h3><p>6 Prawns and Chips</p></div>
<div class="photo" role="img" aria-label="Photo of calamari rings and chips with tartare sauce" style="left:807px"></div>
<div class="badge card-badge" style="left:965px">$14.50</div>

<div class="card" style="left:989px"><h3>Sea Scallop<br>Pack</h3><p>6 Fish Cocktails and Chips</p></div>
<div class="photo" role="img" aria-label="Photo of calamari rings and chips with tartare sauce" style="left:1000px"></div>
<div class="badge card-badge" style="left:1158px">$14.90</div>

<footer class="footer">
  <span>Wild Caught Sustainable Fish | Hand Filleted Onsite | Cooked in 100% Rice Bran Oil | Gluten Free Options Available | Like us on</span>
  <span class="social-name">Shorelink</span>
</footer>
</body>
</html>
```